First Aid Training business needs business card design

We would like a double sided business card designed for a first aid training business - Brindlewood First Aid. We provide first aid training and , WHS (work, health and safety) training.

The attached word document contains the key information we would like on each side of the business card.

Final design needs to be delivered in print ready format, along with the original file.

```html
<!DOCTYPE html>
<html lang="en">
<head>
<meta charset="utf-8">
<title>Brindlewood First Aid – Business Card</title>
<link rel="stylesheet" href="https://fonts.googleapis.com/css2?family=Montserrat:ital,wght@0,400;0,600;0,700;0,800;1,400&display=swap">
<style>
  :root {
    --brand-red: #ed2226;
    --ink: #111111;
    --paper: #ffffff;
    --backdrop: #ececec;
    --text-on-red: #ffffff;
  }
  * { margin: 0; padding: 0; box-sizing: border-box; }
  html, body {
    width: 1200px; height: 1134px; overflow: hidden;
    background: var(--backdrop);
    font-family: "Montserrat", Arial, sans-serif;
  }
  .sheet {
    position: relative; width: 1200px; height: 1134px;
  }
  .card {
    position: absolute; left: 160px; width: 880px; height: 503px;
    background: var(--paper); overflow: hidden;
    box-shadow: 0 10px 30px rgba(0,0,0,0.12);
  }
  .card--front { top: 44px; }
  .card--back { top: 587px; }

  /* Brand name block */
  .brand {
    display: flex; align-items: center; gap: 18px;
    color: var(--ink); font-weight: 800;
  }
  .brand__dot {
    width: 46px; height: 46px; border-radius: 50%;
    background: var(--brand-red); flex: none;
  }
  .brand__name {
    font-size: 40px; line-height: 1.05; letter-spacing: 0.5px;
    text-transform: uppercase;
  }
  .brand__name small {
    display: block; font-size: 19px; letter-spacing: 1.5px;
  }

  /* Front */
  .front__logo-area {
    position: absolute; left: 0; top: 0; width: 100%; height: 250px;
    display: flex; align-items: center; justify-content: center;
  }
  .front__band {
    position: absolute; left: 0; bottom: 0; width: 100%; height: 253px;
    background: var(--brand-red); color: var(--text-on-red);
  }
  .holder {
    position: absolute; left: 48px; top: 40px;
  }
  .holder__name {
    font-size: 38px; font-weight: 700; letter-spacing: 1.5px;
    text-transform: uppercase;
  }
  .contact-line {
    display: flex; align-items: center; gap: 12px;
    font-size: 19px; font-weight: 400; letter-spacing: 0.5px;
  }
  .holder .contact-line { margin-top: 8px; }
  .contact-list {
    position: absolute; right: 48px; bottom: 44px;
    display: flex; flex-direction: column; gap: 10px;
  }
  .icon { width: 20px; height: 20px; flex: none; }

  /* Back */
  .back__panel {
    position: absolute; left: 0; top: 0; width: 540px; height: 100%;
    background: var(--brand-red); color: var(--text-on-red);
    padding: 70px 40px 0 48px;
  }
  .services { list-style: none; }
  .services li { font-size: 21px; line-height: 1.55; }
  .service--main { font-weight: 700; }
  .service--main::before { content: "•"; margin-right: 10px; }
  .service--main em { font-weight: 400; font-style: normal; font-size: 17px; }
  .service--sub { padding-left: 26px; font-weight: 400; }
  .service--sub::before { content: "+"; font-weight: 800; margin-right: 10px; }
  .back__logo-area {
    position: absolute; left: 540px; top: 0; right: 0; height: 100%;
    display: flex; align-items: center; justify-content: center;
  }
  .back__logo-area .brand { flex-direction: column; text-align: center; gap: 14px; }
  .back__logo-area .brand__name { font-size: 30px; }
  .back__logo-area .brand__name small { font-size: 15px; }
</style>
</head>
<body>
<main class="sheet">

  <section class="card card--front" aria-label="Business card front">
    <div class="front__logo-area">
      <div class="brand">
        <span class="brand__dot"></span>
        <span class="brand__name">Brindlewood<small>First Aid Training</small></span>
      </div>
    </div>
    <div class="front__band">
      <div class="holder">
        <p class="holder__name">Daniel Hartley</p>
        <p class="contact-line">
          <svg class="icon" viewBox="0 0 24 24" aria-hidden="true"><path fill="currentColor" d="M6.6 10.8a15.1 15.1 0 0 0 6.6 6.6l2.2-2.2a1 1 0 0 1 1-.25 11.4 11.4 0 0 0 3.6.57 1 1 0 0 1 1 1V20a1 1 0 0 1-1 1A17 17 0 0 1 3 4a1 1 0 0 1 1-1h3.5a1 1 0 0 1 1 1c0 1.25.2 2.45.57 3.57a1 1 0 0 1-.25 1z"/></svg>
          0491 570 226
        </p>
      </div>
      <div class="contact-list">
        <p class="contact-line">
          <svg class="icon" viewBox="0 0 24 24" aria-hidden="true"><path fill="currentColor" d="M3 5h18a1 1 0 0 1 1 1v12a1 1 0 0 1-1 1H3a1 1 0 0 1-1-1V6a1 1 0 0 1 1-1zm9 7.2L4 7.3V8l8 5 8-5v-.7z"/></svg>
          help@brindlewoodfirstaid.com.au
        </p>
        <p class="contact-line">
          <svg class="icon" viewBox="0 0 24 24" aria-hidden="true"><g fill="none" stroke="currentColor" stroke-width="1.8"><circle cx="12" cy="12" r="9"/><ellipse cx="12" cy="12" rx="4" ry="9"/><path d="M3 12h18M5 7h14M5 17h14"/></g></svg>
          www.brindlewoodfirstaid.com.au
        </p>
      </div>
    </div>
  </section>

  <section class="card card--back" aria-label="Business card back">
    <div class="back__panel">
      <ul class="services">
        <li class="service--main">Onsite Training <em>– We can come to you</em></li>
        <li class="service--sub">Time efficient</li>
        <li class="service--sub">Cost effective</li>
        <li class="service--sub">Minimise downtime for your team</li>
        <li class="service--main">First Aid Training</li>
        <li class="service--main">WHS Training</li>
      </ul>
    </div>
    <div class="back__logo-area">
      <div class="brand">
        <span class="brand__dot"></span>
        <span class="brand__name">Brindlewood<small>First Aid Training</small></span>
      </div>
    </div>
  </section>

</main>
</body>
</html>
```